Need a FLAT UI design for mobile campus Marketplace APP

We need to improve our current UI/UX design for a mobile application called Tradlo. It is designed for students to buy and sell their goods, such as books and furnitures, on their own campus to save living expenses. Our initial design does not look very flat and clear enough. We would like to see a flat design improvement for a better purchasing and selling experience using yellow as theme color.

Target Market(s)

college students

Industry/Entity Type

Marketplace

Colors
ffc214
ffcf3e
fee18a
fff3d1

Requirements
Must have
• an improved UI look, flat and simple.
Nice to have
• alternative designs
Should not have
• a new function design for the app on the design

```html
<!DOCTYPE html>
<html lang="en">
<head>
<meta charset="utf-8">
<title>Tradlo – Campus Marketplace</title>
<link href="https://fonts.googleapis.com/css2?family=Lato:wght@300;400;700&family=Montserrat:wght@300;600;700&display=swap" rel="stylesheet">
<style>
:root{
  --page:#efefef;
  --status:#c4a733;
  --bar:#ffd941;
  --accent:#ffc214;
  --tile:#ffffff;
  --gutter:#ececec;
  --text:#6d6d6d;
  --muted:#9a9a9a;
  --icon:#c9c9c9;
  --nav-icon:#8f8f8f;
  --buy:#b02a8f;
}
*{box-sizing:border-box;margin:0;padding:0}
html,body{width:1200px;height:1000px;overflow:hidden}
body{background:var(--page);font-family:"Lato",sans-serif;position:relative}
.screen{position:absolute;top:135px;width:412px;height:730px;background:var(--gutter);overflow:hidden;box-shadow:0 22px 40px rgba(0,0,0,.16)}
.screen--home{left:124px}
.screen--search{left:660px}
.status-bar{height:27px;background:var(--status)}
.app-bar{height:62px;background:var(--bar);position:relative;display:flex;align-items:center;padding:0 20px}
.brand{display:flex;align-items:center;gap:10px;color:#fff;font-weight:700;font-size:19px}
.brand-dot{width:30px;height:30px;border-radius:50%;border:2.5px solid #fff}
.app-actions{margin-left:auto;display:flex;gap:18px;align-items:center}
.app-actions svg{display:block}
.back{display:block}
.search-label{margin-left:auto;color:#fff;font-size:18px;margin-right:14px}
/* banner */
.banner{height:196px;position:relative;background:linear-gradient(90deg,#dedad7,#e6e2df 60%,#ebe8e5)}
.banner-photo{position:absolute;right:0;top:0;width:220px;height:196px;background:radial-gradient(ellipse at 60% 45%,#8a7b8c 0%,#b9b3b0 35%,#d9d4cf 70%,transparent 100%)}
.banner-copy{position:absolute;left:32px;top:24px;font-family:"Montserrat",sans-serif}
.banner-percent{font-weight:300;font-size:38px;color:#c9c3bf;line-height:1}
.banner-title{font-weight:700;font-size:21px;color:#8a8a8a;margin-top:6px;line-height:1.15}
.banner-sub{font-weight:300;font-size:21px;color:#8a8a8a;line-height:1.1}
.banner-cta{display:flex;align-items:center;gap:18px;margin-top:14px}
.banner-price{color:#fff;font-weight:700;font-size:18px}
.btn-buy{background:var(--buy);color:#fff;font-family:"Lato",sans-serif;font-weight:700;font-size:10px;border-radius:11px;padding:4px 10px}
.dots{position:absolute;left:166px;top:179px;display:flex;gap:8px}
.dots span{width:6px;height:6px;border-radius:50%;background:#f5f5f5}
.dots span.on{background:none;border:1.5px solid var(--accent);width:8px;height:8px;margin-top:-1px}
/* categories */
.categories{display:grid;grid-template-columns:134px 136px 134px;grid-template-rows:190px 187px;gap:5px 4px;margin-top:3px}
.category{background:var(--tile);position:relative;text-align:center}
.category svg{position:absolute;left:50%;top:70px;transform:translateX(-50%)}
.category-name{position:absolute;left:0;right:0;top:150px;font-size:12px;color:var(--text)}
/* nav */
.tab-bar{position:absolute;left:0;right:0;bottom:0;height:55px;background:#fafafa;border-top:1px solid #e4e4e4;display:flex;justify-content:space-around;align-items:center;padding:0 12px}
/* search */
.tools{height:46px;background:#fff;display:flex;align-items:center;justify-content:space-around;font-size:14px;color:var(--text);border-bottom:1px solid #e6e6e6}
.tool{display:flex;align-items:center;gap:10px}
.products{display:grid;grid-template-columns:134px 134px 134px;grid-auto-rows:189px;gap:6px 4px;margin-top:5px;height:540px;overflow:hidden}
.product{background:#fff;position:relative;text-align:center}
.product-photo{position:absolute;left:50%;top:14px;width:84px;height:106px;transform:translateX(-50%);border-radius:4px}
.photo-tab{background:linear-gradient(90deg,#c9c9c9,#d9c7a4 40%,#2b2b2b 70%,#5b8fa6)}
.photo-phone{background:linear-gradient(90deg,#e9c3b6 30%,#1e1e1e 45%,#c8321b 75%,#1e1e1e)}
.photo-kit{background:linear-gradient(90deg,#d8d8d8,#2c2c2c 40%,#3a3a3a 70%,#c82b2b)}
.badge{position:absolute;right:6px;top:8px}
.product-name{position:absolute;left:0;right:0;top:146px;font-size:11px;color:var(--muted)}
.product-price{position:absolute;left:0;right:0;top:166px;font-size:13px;color:var(--accent)}
</style>
</head>
<body>

<section class="screen screen--home">
  <div class="status-bar"></div>
  <header class="app-bar">
    <div class="brand"><span class="brand-dot"></span>Tradlo</div>
    <div class="app-actions">
      <svg width="22" height="22" viewBox="0 0 22 22" fill="none" stroke="#fff" stroke-width="3"><circle cx="9" cy="9" r="7"/><path d="M14 14l6 6" stroke-linecap="round"/></svg>
      <svg width="24" height="22" viewBox="0 0 24 22" fill="none" stroke="#fff" stroke-width="2.5"><path d="M1 3h4l3 11h12l2-8H7"/><circle cx="10" cy="19" r="1.6" fill="#fff"/><circle cx="18" cy="19" r="1.6" fill="#fff"/></svg>
    </div>
  </header>

  <div class="banner">
    <div class="banner-photo" role="img" aria-label="Open silver laptop with colourful screen"></div>
    <div class="banner-copy">
      <div class="banner-percent">70%</div>
      <div class="banner-title">NEW YEAR</div>
      <div class="banner-sub">DISCOUNT</div>
      <div class="banner-cta"><span class="banner-price">$600</span><span class="btn-buy">Buy Now</span></div>
    </div>
    <div class="dots"><span class="on"></span><span></span><span></span><span></span><span></span><span></span></div>
  </div>

  <div class="categories">
    <div class="category">
      <svg width="54" height="40" viewBox="0 0 54 40" fill="none" stroke="var(--icon)" stroke-width="1.5"><path d="M2 12L27 2l25 10-25 10z"/><path d="M12 17v12c6 6 24 6 30 0V17"/><path d="M47 14v14"/></svg>
      <div class="category-name">Campus Life</div>
    </div>
    <div class="category">
      <svg width="26" height="40" viewBox="0 0 26 40" fill="none" stroke="var(--icon)" stroke-width="1.5"><rect x="2" y="1" width="22" height="38" rx="3"/><path d="M2 7h22M2 32h22"/><circle cx="13" cy="35.5" r="1.5"/></svg>
      <div class="category-name">Electronics</div>
    </div>
    <div class="category">
      <svg width="38" height="38" viewBox="0 0 38 38" fill="none" stroke="var(--icon)" stroke-width="1.5"><circle cx="19" cy="19" r="17"/><path d="M19 9v10h8"/></svg>
      <div class="category-name">Recents</div>
    </div>
    <div class="category">
      <svg width="42" height="40" viewBox="0 0 42 40" fill="none" stroke="var(--icon)" stroke-width="1.5"><rect x="4" y="2" width="32" height="9"/><rect x="2" y="15" width="36" height="9"/><rect x="6" y="28" width="34" height="9"/><path d="M12 2v9M8 15v9M14 28v9"/></svg>
      <div class="category-name">Books</div>
    </div>
    <div class="category">
      <svg width="50" height="48" viewBox="0 0 50 48" fill="none" stroke="var(--icon)" stroke-width="1.5"><path d="M4 30L30 4l6 6a4 4 0 006 6l4 4-26 26-4-4a4 4 0 00-6-6z"/><path d="M22 14l14 14" stroke-dasharray="3 3"/></svg>
      <div class="category-name">Tickets</div>
    </div>
    <div class="category">
      <svg width="40" height="12" viewBox="0 0 40 12" fill="none" stroke="var(--icon)" stroke-width="1.5"><circle cx="6" cy="6" r="4.5"/><circle cx="20" cy="6" r="4.5"/><circle cx="34" cy="6" r="4.5"/></svg>
      <div class="category-name">Others</div>
    </div>
  </div>

  <nav class="tab-bar">
    <svg width="26" height="24" viewBox="0 0 26 24"><path d="M13 1L1 12h3v11h7v-7h4v7h7V12h3z" fill="var(--accent)"/></svg>
    <svg width="26" height="18" viewBox="0 0 26 18" fill="none" stroke="var(--nav-icon)" stroke-width="1.5"><path d="M1 6h23l-5-5M25 12H2l5 5"/></svg>
    <svg width="22" height="22" viewBox="0 0 22 22" stroke="var(--nav-icon)" stroke-width="2.2"><path d="M11 1v20M1 11h20"/></svg>
    <svg width="26" height="24" viewBox="0 0 26 24" fill="none" stroke="var(--nav-icon)" stroke-width="1.5"><path d="M13 2C6.5 2 2 6 2 11c0 2.5 1 4.5 3 6l-1 5 5-3c1.3.4 2.6.6 4 .6 6.5 0 11-4 11-9S19.5 2 13 2z"/><circle cx="8.5" cy="11" r="1" fill="var(--nav-icon)"/><circle cx="13" cy="11" r="1" fill="var(--nav-icon)"/><circle cx="17.5" cy="11" r="1" fill="var(--nav-icon)"/></svg>
    <svg width="24" height="24" viewBox="0 0 24 24" fill="none" stroke="var(--nav-icon)" stroke-width="1.5"><circle cx="12" cy="8" r="6"/><path d="M1 23c0-5 5-8 11-8s11 3 11 8z"/></svg>
  </nav>
</section>

<section class="screen screen--search">
  <div class="status-bar"></div>
  <header class="app-bar">
    <svg class="back" width="30" height="20" viewBox="0 0 30 20" fill="none" stroke="#fff" stroke-width="2.5" stroke-linecap="round"><path d="M28 10H3M11 2l-8 8 8 8"/></svg>
    <span class="search-label">Search</span>
    <svg width="22" height="22" viewBox="0 0 22 22" fill="none" stroke="#fff" stroke-width="3"><circle cx="9" cy="9" r="7"/><path d="M14 14l6 6" stroke-linecap="round"/></svg>
  </header>

  <div class="tools">
    <span class="tool"><svg width="11" height="11" viewBox="0 0 11 11" fill="var(--accent)"><rect width="5" height="5"/><rect x="6" width="5" height="5"/><rect y="6" width="5" height="5"/><rect x="6" y="6" width="5" height="5"/></svg>Category</span>
    <span class="tool"><svg width="11" height="11" viewBox="0 0 11 11" fill="#777"><path d="M0 0h11L7 5v6L4 9V5z"/></svg>Filters</span>
    <span class="tool"><svg width="9" height="13" viewBox="0 0 9 13" fill="#777"><path d="M4.5 0L9 5H0zM0 8h9l-4.5 5z"/></svg>By Price</span>
  </div>

  <div class="products">
    <div class="product"><div class="product-photo photo-tab" role="img" aria-label="Tablet in silver, gold and black"></div><svg class="badge" width="13" height="16" viewBox="0 0 13 16"><path d="M0 0h13v16l-6.5-4L0 16z" fill="var(--accent)"/></svg><div class="product-name">Nova Tab 32 Gb</div><div class="product-price">$ 299.00</div></div>
    <div class="product"><div class="product-photo photo-phone" role="img" aria-label="Rose gold and black smartphones"></div><svg class="badge" width="13" height="16" viewBox="0 0 13 16"><path d="M0 0h13v16l-6.5-4L0 16z" fill="var(--accent)"/></svg><div class="product-name">Orbit 7 64 Gb</div><div class="product-price">$ 789.00</div></div>
    <div class="product"><div class="product-photo photo-kit" role="img" aria-label="Black smartphone with box and earphones"></div><svg class="badge" width="13" height="16" viewBox="0 0 13 16"><path d="M0 0h13v16l-6.5-4L0 16z" fill="var(--accent)"/></svg><div class="product-name">Pulse 3T 64 Gb</div><div class="product-price">$ 499.00</div></div>
    <div class="product"><div class="product-photo photo-tab" role="img" aria-label="Tablet in silver, gold and black"></div><svg class="badge" width="13" height="16" viewBox="0 0 13 16"><path d="M0 0h13v16l-6.5-4L0 16z" fill="var(--accent)"/></svg><div class="product-name">Nova Tab 32 Gb</div><div class="product-price">$ 299.00</div></div>
    <div class="product"><div class="product-photo photo-phone" role="img" aria-label="Rose gold and black smartphones"></div><svg class="badge" width="13" height="16" viewBox="0 0 13 16"><path d="M0 0h13v16l-6.5-4L0 16z" fill="var(--accent)"/></svg><div class="product-name">Orbit 7 64 Gb</div><div class="product-price">$ 789.00</div></div>
    <div class="product"><div class="product-photo photo-kit" role="img" aria-label="Black smartphone with box and earphones"></div><svg class="badge" width="13" height="16" viewBox="0 0 13 16"><path d="M0 0h13v16l-6.5-4L0 16z" fill="var(--accent)"/></svg><div class="product-name">Pulse 3T 64 Gb</div><div class="product-price">$ 499.00</div></div>
    <div class="product"><div class="product-photo photo-tab" role="img" aria-label="Tablet in silver, gold and black"></div><svg class="badge" width="13" height="16" viewBox="0 0 13 16"><path d="M0 0h13v16l-6.5-4L0 16z" fill="var(--accent)"/></svg></div>
    <div class="product"><div class="product-photo photo-phone" role="img" aria-label="Rose gold and black smartphones"></div><svg class="badge" width="13" height="16" viewBox="0 0 13 16"><path d="M0 0h13v16l-6.5-4L0 16z" fill="var(--accent)"/></svg></div>
    <div class="product"><div class="product-photo photo-kit" role="img" aria-label="Black smartphone with box and earphones"></div><svg class="badge" width="13" height="16" viewBox="0 0 13 16"><path d="M0 0h13v16l-6.5-4L0 16z" fill="var(--accent)"/></svg></div>
  </div>

  <nav class="tab-bar">
    <svg width="26" height="24" viewBox="0 0 26 24"><path d="M13 1L1 12h3v11h7v-7h4v7h7V12h3z" fill="var(--accent)"/></svg>
    <svg width="26" height="18" viewBox="0 0 26 18" fill="none" stroke="var(--nav-icon)" stroke-width="1.5"><path d="M1 6h23l-5-5M25 12H2l5 5"/></svg>
    <svg width="22" height="22" viewBox="0 0 22 22" stroke="var(--nav-icon)" stroke-width="2.2"><path d="M11 1v20M1 11h20"/></svg>
    <svg width="26" height="24" viewBox="0 0 26 24" fill="none" stroke="var(--nav-icon)" stroke-width="1.5"><path d="M13 2C6.5 2 2 6 2 11c0 2.5 1 4.5 3 6l-1 5 5-3c1.3.4 2.6.6 4 .6 6.5 0 11-4 11-9S19.5 2 13 2z"/><circle cx="8.5" cy="11" r="1" fill="var(--nav-icon)"/><circle cx="13" cy="11" r="1" fill="var(--nav-icon)"/><circle cx="17.5" cy="11" r="1" fill="var(--nav-icon)"/></svg>
    <svg width="24" height="24" viewBox="0 0 24 24" fill="none" stroke="var(--nav-icon)" stroke-width="1.5"><circle cx="12" cy="8" r="6"/><path d="M1 23c0-5 5-8 11-8s11 3 11 8z"/></svg>
  </nav>
</section>

</body>
</html>
```